Harbourline Coldworks Tri-fold Information Brochure

Looking for a sleek, clean and professional design for a tri-fold brochure so people can learn about Harbourline Coldworks, understand what Cryotherapy is, and what it can do for them.

Will be printed using pressly cards (dimensions provided on their website say the tri-fold will be 8.5" x 11" {279 x 216 mm})

Include out website: www.harbourlinecoldworks.ca:
social media handles
Facebook and Instagram: @Harbourlinecoldworks
Twitter: @HarbCold

Sections- Below I will provide copyright and sections that must be included in the brochure. The title of the sections can be modified (lengthened or shortened) to provide the best look.

Benefits:
Pain Management
Injury Therapy
Rapid Recovery
Performance
Metabolic Boost
Immunity Boost
Anti-Aging
Skin Rejevenation

Applications:
Athletic Performance
Post-surgical Recovery
Musculosketetal Injuries
Rheumatoid Arthritis
Caloric Burn
Skin Disorders
Autoimmune and Other Inflammatory Disorders

Used by professional athletes: logos for the PBL, GFA, RKA, DBU, KSF, WJX, TWE Circuit

As seen on TV: Logos for Dr. Quill Hour, Bright Dawn Daily, TVK, WJR Games, Wanderlight Network, QP, The Healers, KRT Report

Customized Treatment Protocols

Just 3 Minutes

FAQs

How Does Cryotherapy Work?
Whole body skin exposure to the ultra-low temperatures -145°C to -165°C (-229°F to -265°F) triggers a systemic anti-inflammatory response that activates organs, muscles, joints, and skin to heal and repair themselves. The result is a dramatic increase in circulation, metabolism, tissue repair, detoxification and immune function.

Is it comfortable?
The treatment is short and the cold air has no moisture present, so it's very tolerable and much easier to do compared to an ice bath or cold shower. Towards the end of the treatment, you may get a "pins and needles" sensation that disappears immediately after the treatment.

Is it safe?
No, the liquid nitrogen that is used as a chilling agent does not come into contact with your skin. Nitrogen is nontoxic, and nonflammable it comprises 78% of the air we breathe. A trained operator is always present during the treatment to control the temperature and monitor your comfort. There are no locks or latches on the door so you are able exit the cryochamber easily and quickly anytime.

How do I feel after a treatment?
the brisk exhilaration causes your brain to release high amounts of endorphin and norepinephrine, which make you feel good and focused. Most people report feeling energetic and full of like. The buoyant effects from each session peak after many hours and may last for weeks.

Target Market(s)

People that stay active and are looking to take advantage of the benefits of cryotherapy. People with chronic or acute conditions looking to accelerate and help with recovery and treatment.

Industry/Entity Type

Health And Wellness

Font styles to use
Sans Serif

Colors
ffffff
000000
57b5de

Requirements
Must have
• Use logo colors (white, black and blue) the shade of blue to be used must be as close to the logo's shade of blue as possible.
• A picture of the machine that has been provided or a picture of a similar looking machine from online.
Nice to have
• Mountains or mist
• a person running/being active
• a person doing yoga or a women boxing
• a picture signifying joint pain

```html
<!DOCTYPE html>
<html lang="en">
<head>
<meta charset="utf-8">
<title>Harbourline Coldworks – Tri-fold Brochure</title>
<link href="https://fonts.googleapis.com/css2?family=Bitter:wght@600;700;800;900&family=Open+Sans:wght@400;600;700&display=swap" rel="stylesheet">
<style>
:root{
  --blue:#2f8fd0;
  --blue-light:#57b5de;
  --blue-pale:#a9d8ef;
  --ink:#3b3b3b;
  --ink-soft:#6d6d6d;
  --paper:#ffffff;
  --grey-panel:#e4e4e4;
  --icon-box:#4a4a4a;
  --backdrop:#e8eaed;
}
*{margin:0;padding:0;box-sizing:border-box}
html,body{width:1200px;height:960px;overflow:hidden}
body{background:var(--backdrop);font-family:"Open Sans",sans-serif;color:var(--ink);position:relative}
.sheet{position:absolute;top:255px;width:582px;height:450px;background:var(--paper);overflow:hidden;box-shadow:0 4px 18px rgba(0,0,0,.18)}
.sheet--inside{left:12px}
.sheet--outside{left:606px}
.fold{position:absolute;top:0;bottom:0;width:1px;background:rgba(0,0,0,.06)}
.abs{position:absolute}
.photo{position:absolute}
.slab{font-family:"Bitter",serif}

/* inside */
.photo--boxer{left:0;top:0;width:582px;height:152px;background:linear-gradient(120deg,#8f9193 0%,#b8b6b2 35%,#d8c2b0 52%,#a7a8aa 75%,#c9cacc 100%);clip-path:polygon(0 0,582px 0,582px 14px,436px 152px,0 152px)}
.panel-title{font-family:"Bitter",serif;font-weight:700;font-size:11px;letter-spacing:.6px;text-transform:uppercase;color:var(--ink)}
.benefits-title{left:0;width:194px;top:170px;text-align:center}
.benefits-intro{left:12px;top:198px;width:58px;font-size:5.6px;line-height:1.35;color:var(--ink-soft)}
.benefits-list{left:74px;top:196px;width:110px;background:var(--blue-light);padding:7px 8px;list-style:none}
.benefits-list li{font-family:"Bitter",serif;font-size:7.6px;color:#fff;line-height:1.55;border-bottom:1px solid rgba(255,255,255,.35)}
.benefits-list li:last-child{border-bottom:0}
.photo--knee{left:20px;top:300px;width:92px;height:120px;background:radial-gradient(circle at 60% 45%,#f0a9a4 0%,#e9d5cf 25%,#f4f2f1 60%,#e3e3e3 100%)}
.photo--chamber{left:104px;top:326px;width:90px;height:124px;background:linear-gradient(160deg,#cfd3d6,#8e959b 55%,#5f6469)}

.faq-title{left:200px;top:160px}
.faq{position:absolute;left:200px;width:186px;display:flex;gap:6px}
.faq-label{width:44px;flex:none}
.faq-icon{width:24px;height:22px;background:var(--icon-box);display:flex;align-items:center;justify-content:center}
.faq-q{font-family:"Bitter",serif;font-weight:700;font-size:6.8px;line-height:1.15;text-transform:uppercase;margin-top:3px}
.faq-a{font-size:5.3px;line-height:1.3;color:var(--ink-soft)}

.applications-title{left:400px;top:170px}
.applications-list{left:404px;top:198px;width:172px;list-style:none}
.applications-list li{display:flex;align-items:flex-start;gap:7px;font-family:"Bitter",serif;font-weight:700;font-size:7.6px;line-height:1.2;margin-bottom:9px;color:var(--ink)}
.applications-list svg{flex:none;margin-top:-1px}

/* outside */
.headline{font-family:"Bitter",serif;font-weight:900;text-transform:uppercase;color:var(--ink);letter-spacing:.8px;line-height:1.05}
.athletes-title{left:14px;top:20px;font-size:12px;width:170px}
.mark-row{position:absolute;left:14px;width:172px;display:flex;flex-wrap:wrap;gap:4px 6px;align-items:center}
.mark{font-family:"Bitter",serif;font-weight:800;font-size:8px;color:var(--ink);display:flex;align-items:center;gap:2px}
.mark i{display:inline-block;width:6px;height:6px;background:var(--blue)}
.athlete-marks{top:66px}
.tv-title{left:14px;top:112px;font-size:12px}
.tv-marks{top:132px}
.protocols{left:14px;top:190px;font-size:14px;width:170px}
.minutes{left:14px;top:252px;font-size:12.5px}
.photo--dancer{left:0;top:318px;width:194px;height:132px;background:linear-gradient(180deg,#1c1c1c 0%,#2a2523 55%,#c9a88f 100%);clip-path:polygon(0 30px,194px 0,194px 132px,0 132px)}
.corner-blue{left:0;top:380px}

.bubble{left:214px;top:40px;width:154px;height:104px;background:var(--grey-panel);text-align:center;padding-top:12px}
.bubble-tail{left:318px;top:143px}
.smiley{width:18px;height:18px;border-radius:50%;background:#9a9a9a;margin:0 auto 6px;display:flex;align-items:center;justify-content:center}
.bubble h3{font-family:"Bitter",serif;font-weight:600;font-size:8px;letter-spacing:.6px;color:var(--ink)}
.dash{width:18px;height:2px;background:var(--blue);margin:5px auto}
.bubble p{font-size:5.8px;color:var(--ink-soft)}
.contact{left:196px;top:276px;width:190px;text-align:center}
.contact h3{font-family:"Bitter",serif;font-weight:700;font-size:9px;letter-spacing:.6px}
.contact .label{font-size:7px;color:var(--ink-soft);margin-top:8px}
.contact .value{font-size:7px;color:var(--ink);font-weight:600}

.photo--peaks{left:388px;top:0;width:194px;height:450px;background:linear-gradient(170deg,#8ea6b7 0%,#dfe6ea 30%,#f3f5f6 48%,#b9c6cf 70%,#eef1f3 100%)}
.logo-band{left:394px;top:84px;width:188px;height:32px;background:#fff;display:flex;align-items:center;gap:6px;padding-left:10px}
.logo-square{width:14px;height:14px;background:var(--blue-light)}
.logo-name{font-family:"Bitter",serif;font-weight:700;font-size:9.5px;line-height:1;text-transform:uppercase;color:var(--ink)}
.cover-blue{left:388px;top:0}
.cover-kicker{right:14px;top:306px;font-family:"Bitter",serif;font-size:7.5px;letter-spacing:.6px;color:#fff;text-transform:uppercase}
.cover-title{right:14px;top:318px;font-family:"Bitter",serif;font-weight:800;font-size:16px;line-height:1.05;color:#fff;text-transform:uppercase;text-align:right}
.cover-text{right:12px;top:362px;width:160px;font-size:5.6px;line-height:1.35;color:#fff;text-align:right}
</style>
</head>
<body>

<!-- Inside spread -->
<section class="sheet sheet--inside">
  <div class="photo photo--boxer" role="img" aria-label="Woman with braided hair boxing in front of a stone wall"></div>
  <svg class="abs" style="left:0;top:0" width="582" height="450" aria-hidden="true">
    <polygon points="582,14 582,128 448,152 436,152" fill="var(--blue)"/>
    <polygon points="582,0 582,14 436,152 420,152" fill="var(--blue-light)"/>
    <polygon points="0,152 58,152 0,186" fill="var(--blue)"/>
    <polygon points="58,152 78,152 0,198 0,186" fill="var(--blue-light)"/>
  </svg>
  <div class="fold" style="left:194px"></div>
  <div class="fold" style="left:388px"></div>

  <h2 class="abs panel-title benefits-title">Benefits</h2>
  <p class="abs benefits-intro">Harbourline Coldworks is dedicated to leveraging cryo in the most effective ways possible for you.</p>
  <ul class="abs benefits-list">
    <li>Pain Management</li><li>Injury Therapy</li><li>Rapid Recovery</li><li>Performance</li>
    <li>Metabolic Boost</li><li>Immunity Boost</li><li>Anti-Aging</li><li>Skin Rejevenation</li>
  </ul>
  <div class="photo photo--knee" role="img" aria-label="Hands holding a painful knee joint"></div>
  <div class="photo photo--chamber" role="img" aria-label="Whole body cryotherapy chamber"></div>

  <h2 class="abs panel-title faq-title">FAQs</h2>
  <div class="faq" style="top:180px">
    <div class="faq-label">
      <div class="faq-icon"><svg width="12" height="12" viewBox="0 0 12 12"><circle cx="5" cy="5" r="3.3" fill="none" stroke="#fff" stroke-width="1.4"/><line x1="7.5" y1="7.5" x2="11" y2="11" stroke="#fff" stroke-width="1.6"/></svg></div>
      <div class="faq-q">How it works</div>
    </div>
    <p class="faq-a">Whole body skin exposure to the ultra-low temperatures -145°C to -165°C (-229°F to -265°F) triggers a systemic anti-inflammatory response that activates organs, muscles, joints, and skin to heal and repair themselves. The result is a dramatic increase in circulation, metabolism, tissue repair, detoxification and immune function.</p>
  </div>
  <div class="faq" style="top:244px">
    <div class="faq-label">
      <div class="faq-icon"><svg width="12" height="12" viewBox="0 0 12 12"><path d="M2 2h8L6 7v4M4 11h4" fill="none" stroke="#fff" stroke-width="1.3"/></svg></div>
      <div class="faq-q">Is it comfortable?</div>
    </div>
    <p class="faq-a">The treatment is short and the cold air has no moisture present, so it's very tolerable and much easier to do compared to an ice bath or cold shower. Towards the end of the treatment, you may get a "pins and needles" sensation that disappears immediately after the treatment.</p>
  </div>
  <div class="faq" style="top:300px">
    <div class="faq-label">
      <div class="faq-icon"><svg width="12" height="12" viewBox="0 0 12 12"><path d="M6 1l4.5 2v3c0 2.6-2 4.3-4.5 5C3.5 10.3 1.5 8.6 1.5 6V3z" fill="none" stroke="#fff" stroke-width="1.2"/><path d="M4 6l1.5 1.5L8.2 4.6" fill="none" stroke="#fff" stroke-width="1.2"/></svg></div>
      <div class="faq-q">Is it safe?</div>
    </div>
    <p class="faq-a">No, the liquid nitrogen that is used as a chilling agent does not come into contact with your skin. Nitrogen is nontoxic, and nonflammable it comprises 78% of the air we breathe. A trained operator is always present during the treatment to control the temperature and monitor your comfort. There are no locks or latches on the door so you are able exit the cryochamber easily and quickly anytime.</p>
  </div>
  <div class="faq" style="top:378px">
    <div class="faq-label">
      <div class="faq-icon"><svg width="12" height="12" viewBox="0 0 12 12"><circle cx="6" cy="6" r="4.8" fill="none" stroke="#fff" stroke-width="1.2"/><circle cx="4.3" cy="5" r=".8" fill="#fff"/><circle cx="7.7" cy="5" r=".8" fill="#fff"/><path d="M3.8 7.3q2.2 2 4.4 0" fill="none" stroke="#fff" stroke-width="1"/></svg></div>
      <div class="faq-q">How do I feel?</div>
    </div>
    <p class="faq-a">The brisk exhilaration causes your brain to release high amounts of endorphin and norepinephrine, which make you feel good and focused. Most people report feeling energetic and full of life. The buoyant effects from each session peak after many hours and may last for weeks.</p>
  </div>

  <h2 class="abs panel-title applications-title">Applications</h2>
  <ul class="abs applications-list">
    <li><svg width="10" height="10" viewBox="0 0 10 10"><circle cx="5" cy="5" r="4.3" fill="none" stroke="#9a9a9a"/><path d="M2.8 5l1.6 1.6L7.4 3.4" fill="none" stroke="#6d6d6d" stroke-width="1.1"/></svg>Athletic Performance</li>
    <li><svg width="10" height="10" viewBox="0 0 10 10"><circle cx="5" cy="5" r="4.3" fill="none" stroke="#9a9a9a"/><path d="M2.8 5l1.6 1.6L7.4 3.4" fill="none" stroke="#6d6d6d" stroke-width="1.1"/></svg>Post-surgical Recovery</li>
    <li><svg width="10" height="10" viewBox="0 0 10 10"><circle cx="5" cy="5" r="4.3" fill="none" stroke="#9a9a9a"/><path d="M2.8 5l1.6 1.6L7.4 3.4" fill="none" stroke="#6d6d6d" stroke-width="1.1"/></svg>Musculosketetal Injuries</li>
    <li><svg width="10" height="10" viewBox="0 0 10 10"><circle cx="5" cy="5" r="4.3" fill="none" stroke="#9a9a9a"/><path d="M2.8 5l1.6 1.6L7.4 3.4" fill="none" stroke="#6d6d6d" stroke-width="1.1"/></svg>Rheumatoid Arthritis</li>
    <li><svg width="10" height="10" viewBox="0 0 10 10"><circle cx="5" cy="5" r="4.3" fill="none" stroke="#9a9a9a"/><path d="M2.8 5l1.6 1.6L7.4 3.4" fill="none" stroke="#6d6d6d" stroke-width="1.1"/></svg>Caloric Burn</li>
    <li><svg width="10" height="10" viewBox="0 0 10 10"><circle cx="5" cy="5" r="4.3" fill="none" stroke="#9a9a9a"/><path d="M2.8 5l1.6 1.6L7.4 3.4" fill="none" stroke="#6d6d6d" stroke-width="1.1"/></svg>Skin Disorders</li>
    <li><svg width="10" height="10" viewBox="0 0 10 10"><circle cx="5" cy="5" r="4.3" fill="none" stroke="#9a9a9a"/><path d="M2.8 5l1.6 1.6L7.4 3.4" fill="none" stroke="#6d6d6d" stroke-width="1.1"/></svg>Autoimmune and Other<br>Inflammatory Disorders</li>
  </ul>
</section>

<!-- Outside spread -->
<section class="sheet sheet--outside">
  <div class="fold" style="left:194px"></div>
  <div class="fold" style="left:388px"></div>

  <h2 class="abs headline athletes-title">Used by<br>professional<br>athletes</h2>
  <div class="mark-row athlete-marks">
    <span class="mark"><i></i>PBL</span><span class="mark"><i></i>RKA</span><span class="mark"><i></i>GFA</span>
    <span class="mark"><i></i>DBU</span><span class="mark"><i></i>KSF</span><span class="mark"><i></i>WJX</span>
    <span class="mark"><i></i>TWE Circuit</span>
  </div>
  <h2 class="abs headline tv-title">As seen on TV</h2>
  <div class="mark-row tv-marks">
    <span class="mark"><i></i>Dr. Quill Hour</span><span class="mark"><i></i>QP</span><span class="mark"><i></i>The Healers</span>
    <span class="mark"><i></i>Bright Dawn Daily</span><span class="mark"><i></i>TVK</span><span class="mark"><i></i>WJR Games</span>
    <span class="mark"><i></i>Wanderlight Network</span><span class="mark"><i></i>KRT Report</span>
  </div>
  <h2 class="abs headline protocols">Customized<br>treatment<br>protocols</h2>
  <h2 class="abs headline minutes">Just 3 minutes</h2>
  <div class="photo photo--dancer" role="img" aria-label="Woman in a red top stretching in a backbend pose"></div>
  <svg class="abs corner-blue" width="120" height="70" aria-hidden="true">
    <polygon points="0,0 100,70 0,70" fill="var(--blue)"/>
    <polygon points="0,0 14,0 120,70 100,70" fill="var(--blue-light)"/>
  </svg>

  <div class="abs bubble">
    <div class="smiley"><svg width="12" height="12" viewBox="0 0 12 12"><circle cx="4.2" cy="4.8" r=".9" fill="#fff"/><circle cx="7.8" cy="4.8" r=".9" fill="#fff"/><path d="M3.5 7.2q2.5 2.2 5 0" fill="none" stroke="#fff" stroke-width="1"/></svg></div>
    <h3>WE ARE HERE FOR YOU</h3>
    <div class="dash"></div>
    <p>Book your session with us today!</p>
  </div>
  <svg class="abs bubble-tail" width="26" height="22" aria-hidden="true"><polygon points="0,0 26,0 24,22" fill="var(--grey-panel)"/></svg>

  <div class="abs contact">
    <h3>GET IN TOUCH</h3>
    <div class="dash"></div>
    <p class="label">Address</p>
    <p class="value">418 Wharfside Lane, Vancouver, BC V6B 0Z4</p>
    <p class="label">Phone</p>
    <p class="value">(555) 014-2796</p>
    <p class="label">Email</p>
    <p class="value">hello@harbourlinecoldworks.ca</p>
    <p class="value" style="margin-top:6px">www.harbourlinecoldworks.ca</p>
  </div>

  <div class="photo photo--peaks" role="img" aria-label="Mountain peaks rising through mist and clouds"></div>
  <svg class="abs cover-blue" width="194" height="450" aria-hidden="true">
    <polygon points="194,170 194,450 0,450" fill="var(--blue)"/>
    <polygon points="194,150 194,170 0,450 0,430 " fill="var(--blue-light)"/>
    <polygon points="0,450 0,400 60,450" fill="var(--blue-pale)" opacity=".6"/>
  </svg>
  <div class="abs logo-band">
    <span class="logo-square"></span>
    <span class="logo-name">Harbourline<br>Coldworks</span>
  </div>
  <p class="abs cover-kicker">Providing the best</p>
  <h1 class="abs cover-title">Cryotherapy<br>Services</h1>
  <p class="abs cover-text">Harbourline Coldworks is the first to bring whole body cryotherapy and its proven health and beauty benefits to Vancouver.</p>
</section>

</body>
</html>
```